Business Card Design - Law Firm

We are a boutique law firm located near the beach in Manly, Australia. We have recently had a new logo designed and are revamping our business cards with the new logo.

We have recently had a business card design done for us but are not entirely happy with it. We are looking for something modern, simplistic but striking. We would like to see multiple designs.

We have attached a word document which includes our new logo and the current business card design which we are looking at moving away from.

We would like the business cards to be double sided. We would like the design to include something which we can print in gloss colour when we send it to the business card printers.

```html
<!DOCTYPE html>
<html lang="en">
<head>
<meta charset="utf-8">
<title>Marlow &amp; Partners Lawyers – Business Card</title>
<link rel="stylesheet" href="https://fonts.googleapis.com/css2?family=Lato:wght@400;700;900&display=swap">
<style>
  :root {
    --backdrop: #1f1f21;
    --card-white: #ffffff;
    --brand-blue: #4d5fa6;
    --ink-dark: #222222;
    --ink-soft: #4a4a4a;
    --on-blue: #ffffff;
  }
  * { margin: 0; padding: 0; box-sizing: border-box; }
  html, body {
    width: 1200px; height: 800px; overflow: hidden;
    background: var(--backdrop);
    font-family: "Lato", sans-serif;
  }
  .canvas { position: relative; width: 1200px; height: 800px; }

  .card {
    position: absolute; left: 347px; width: 513px; height: 293px;
    border-radius: 18px; overflow: hidden;
  }
  .card--front { top: 66px; background: var(--card-white); }
  .card--back  { top: 434px; background: var(--brand-blue); }

  /* Front: firm name block */
  .firm-mark {
    position: absolute; left: 20px; top: 78px; width: 216px; height: 138px;
    display: flex; flex-direction: column; align-items: center; justify-content: center; gap: 14px;
  }
  .firm-mark__dot { width: 34px; height: 34px; border-radius: 50%; background: var(--brand-blue); }
  .firm-mark__name {
    font-weight: 700; font-size: 16px; line-height: 1.25; text-align: center;
    color: var(--brand-blue); letter-spacing: 0.5px;
  }

  .divider {
    position: absolute; left: 256px; top: 78px; width: 1.5px; height: 138px;
    background: var(--brand-blue);
  }

  /* Front: contact details */
  .contact { position: absolute; left: 279px; top: 72px; width: 225px; }
  .contact__name { font-weight: 900; font-size: 24px; color: var(--brand-blue); line-height: 1.05; letter-spacing: -0.3px; }
  .contact__role { font-size: 12.5px; color: var(--ink-dark); margin-top: 3px; }
  .contact__address { font-size: 12px; color: var(--ink-soft); margin-top: 10px; line-height: 1.5; padding-left: 1px; }
  .contact__list { list-style: none; margin-top: 9px; }
  .contact__item {
    display: flex; align-items: center; gap: 7px;
    font-size: 12px; color: var(--ink-soft); line-height: 1.65;
  }
  .contact__icon { width: 11px; height: 11px; flex: none; }

  /* Back */
  .back-mark {
    position: absolute; inset: 0;
    display: flex; flex-direction: column; align-items: center; justify-content: center; gap: 26px;
  }
  .back-mark__dot { width: 96px; height: 96px; border-radius: 50%; background: var(--on-blue); }
  .back-mark__name {
    font-weight: 700; font-size: 30px; line-height: 1.25; text-align: center;
    color: var(--on-blue); letter-spacing: 1.5px;
  }
</style>
</head>
<body>
<main class="canvas">

  <section class="card card--front" aria-label="Business card front">
    <div class="firm-mark">
      <span class="firm-mark__dot"></span>
      <span class="firm-mark__name">Marlow &amp; Partners<br>Lawyers</span>
    </div>

    <span class="divider"></span>

    <div class="contact">
      <h1 class="contact__name">Alice Harmon</h1>
      <p class="contact__role">Practice Manager</p>
      <p class="contact__address">Suite 4, 12 Tidewater Lane<br>SEAVIEW NSW 2100</p>
      <ul class="contact__list">
        <li class="contact__item">
          <svg class="contact__icon" viewBox="0 0 12 12" aria-hidden="true">
            <path fill="#4d5fa6" d="M1 4.2C1 2.6 3 2 6 2s5 .6 5 2.2v.8H8.6V3.8H3.4V5H1z"/>
            <rect x="2" y="5.6" width="8" height="5" rx="1" fill="#4d5fa6"/>
          </svg>
          (02) 9000 4187
        </li>
        <li class="contact__item">
          <svg class="contact__icon" viewBox="0 0 12 12" aria-hidden="true">
            <rect x="0.5" y="2.5" width="11" height="7.5" fill="#4d5fa6"/>
            <path d="M0.8 2.8 6 7l5.2-4.2M0.8 9.7 4.5 6M11.2 9.7 7.5 6" stroke="#fff" stroke-width="0.9" fill="none"/>
          </svg>
          alice.harmon@seawardlaw.com.au
        </li>
        <li class="contact__item">
          <svg class="contact__icon" viewBox="0 0 12 12" aria-hidden="true">
            <g fill="none" stroke="#4d5fa6" stroke-width="0.9">
              <circle cx="6" cy="6" r="5"/>
              <ellipse cx="6" cy="6" rx="2.2" ry="5"/>
              <path d="M1 6h10M1.8 3.5h8.4M1.8 8.5h8.4"/>
            </g>
          </svg>
          www.marlowandpartners.com.au
        </li>
      </ul>
    </div>
  </section>

  <section class="card card--back" aria-label="Business card back">
    <div class="back-mark">
      <span class="back-mark__dot"></span>
      <span class="back-mark__name">Marlow &amp; Partners<br>Lawyers</span>
    </div>
  </section>

</main>
</body>
</html>
```